Business cards for property management company

Need new business cards designed for our property management company and rental community, Blue Fern Commons. These cards will be primarily picked up by rental applicants.

May be single or double sided design.

I need cards for two different people, listed below. The design can be the same for both, and the only information that will be different is name and email address.

Industry/Entity Type

Property Management

Requirements
Must have
• US standard business card - 2''x3.5'' horizontal design.

1. Logo (attached). The text does not have to stay below the logo, but the card does need to say "Blue Fern Commons" somewhere on it (does not have to be same font as logo, but those fonts are Americana Extra Bold and BlackJack if needed).
2. Name: one with "Paula Whitcombe" and one with "Darrell Whitcombe"
3. Email address: one with "paula@bluefernhome.com" and one with "darrell@bluefernhome.com"
4. Web address: bluefernhome.com
5. Phone: 281.604.2218
6. Address: 1783 Wexford Lane, Porterfield, Texas 77812 (zip code may me omitted, at your discretion)
Should not have
• No rounded corners or special cuts.

No bevel, emboss or shadow effects.

As a note, please do not use our website as a basis for color or design schemes. We are working on a redesign, based around the new logo (attached to brief).

```html
<!DOCTYPE html>
<html lang="en">
<head>
<meta charset="utf-8">
<title>Blue Fern Commons – Business Card</title>
<link rel="stylesheet" href="https://fonts.googleapis.com/css2?family=Arimo:wght@400;700&display=swap">
<style>
  :root {
    --page: #2a2b2d;
    --card: #f1f1f0;
    --green: #3b8b36;
    --ink: #5b5b5b;
    --rule: #c9c9c9;
  }
  * { margin: 0; padding: 0; box-sizing: border-box; }
  html, body { width: 1200px; height: 984px; overflow: hidden; }
  body {
    background: var(--page);
    font-family: "Arimo", Arial, sans-serif;
    position: relative;
  }
  .card {
    position: absolute;
    left: 250px;
    width: 700px;
    height: 400px;
    background: var(--card);
  }
  .card-back { top: 56px; }
  .card-front { top: 528px; }

  /* Back side */
  .back-brand {
    position: absolute;
    left: 56px;
    top: 130px;
    font-weight: 700;
    font-size: 46px;
    line-height: 1.1;
    color: var(--green);
  }
  .back-web {
    position: absolute;
    right: 48px;
    bottom: 60px;
    font-size: 22px;
    letter-spacing: 1.5px;
    color: var(--ink);
  }
  .back-web .domain { color: var(--green); font-weight: 700; }

  /* Front side */
  .front-brand {
    position: absolute;
    left: 44px;
    top: 0;
    width: 270px;
    height: 400px;
    display: flex;
    align-items: center;
    justify-content: center;
    text-align: center;
    font-weight: 700;
    font-size: 34px;
    line-height: 1.15;
    color: var(--green);
  }
  .divider {
    position: absolute;
    left: 340px;
    top: 40px;
    width: 1px;
    height: 320px;
    background: var(--rule);
  }
  .contact {
    position: absolute;
    left: 376px;
    top: 84px;
    right: 30px;
    color: var(--ink);
  }
  .person-name {
    font-weight: 700;
    font-size: 27px;
    color: var(--green);
    margin-bottom: 22px;
    margin-left: 40px;
  }
  .line {
    display: flex;
    align-items: flex-start;
    font-size: 19px;
    line-height: 24px;
  }
  .line + .line { margin-top: 2px; }
  .line.address { margin-top: 24px; font-size: 20px; line-height: 26px; }
  .icon {
    width: 18px;
    height: 18px;
    flex: none;
    margin: 3px 14px 0 0;
    fill: var(--green);
  }
</style>
</head>
<body>

  <section class="card card-back" aria-label="Card back">
    <div class="back-brand">Blue Fern<br>Commons</div>
    <p class="back-web">www.<span class="domain">bluefernhome</span>.com</p>
  </section>

  <section class="card card-front" aria-label="Card front">
    <div class="front-brand">Blue Fern Commons</div>
    <div class="divider"></div>
    <div class="contact">
      <p class="person-name">Paula Whitcombe</p>
      <p class="line">
        <svg class="icon" viewBox="0 0 18 18" aria-hidden="true"><rect x="1" y="4" width="16" height="11" rx="1"/><path d="M1.5 4.5 9 10l7.5-5.5" fill="none" stroke="#f1f1f0" stroke-width="1.4"/></svg>
        paula@bluefernhome.com
      </p>
      <p class="line">
        <svg class="icon" viewBox="0 0 18 18" aria-hidden="true"><rect x="2" y="2" width="14" height="15" rx="1.5"/><rect x="4.5" y="4" width="9" height="4" fill="#f1f1f0"/><rect x="4.5" y="10" width="2.5" height="2" fill="#f1f1f0"/><rect x="8" y="10" width="2.5" height="2" fill="#f1f1f0"/><rect x="11.5" y="10" width="2" height="2" fill="#f1f1f0"/><rect x="4.5" y="13" width="2.5" height="2" fill="#f1f1f0"/><rect x="8" y="13" width="2.5" height="2" fill="#f1f1f0"/></svg>
        281.604.2218
      </p>
      <p class="line address">
        <svg class="icon" viewBox="0 0 18 18" aria-hidden="true"><path d="M9 1.5 0.8 9h2.4v7.5h4.3v-5h3v5h4.3V9h2.4z"/></svg>
        <span>1783 Wexford Lane,<br>Porterfield, Texas<br>77812</span>
      </p>
    </div>
  </section>

</body>
</html>
```